The Stone Lantern business cards

Hi
i have attached a photo, this is how i want the front of my business card to look like:
i want the water drop on the right to be orange
and the water drop on the left to be gloss black
"The" and "Pty Ltd." will be in the same orange as the water drop
and "Stone Lantern" will be in white
The background of the logo will be a matte black
on the back of the business card i need the following info:
'The Stone Lantern pty ltd. '
'Plumbing . Drainage . Gas Fitting . Roofing . Jet Blasting . CCTV . '
Also my contact details:
Gus Palmer
0411827396
thestonelantern@mailbarn.example
Licence# 861427D
Target Market(s)
Strata managers, building managers, the general public
Industry/Entity Type
Business

```html
<!DOCTYPE html>
<html lang="en">
<head>
<meta charset="utf-8">
<title>The Stone Lantern – Business Card Back</title>
<link href="https://fonts.googleapis.com/css2?family=Arvo:wght@400;700&display=swap" rel="stylesheet">
<style>
  :root {
    --orange: #f26a21;
    --ink: #1c1c1c;
    --card: #f7f7f5;
    --backdrop: #e4e5e7;
  }
  * { margin: 0; padding: 0; box-sizing: border-box; }
  html, body {
    width: 1200px;
    height: 676px;
    overflow: hidden;
    background: var(--backdrop);
  }
  .canvas {
    width: 1200px;
    height: 676px;
    display: flex;
    align-items: center;
    justify-content: center;
  }
  .card {
    position: relative;
    width: 900px;
    height: 550px;
    background: var(--card);
    font-family: "Arvo", Georgia, serif;
    color: var(--ink);
    box-shadow: 0 2px 10px rgba(0,0,0,0.12);
  }
  .masthead {
    position: absolute;
    left: 56px;
    right: 40px;
    top: 150px;
  }
  .masthead-row {
    display: flex;
    align-items: flex-start;
  }
  .company-name {
    font-size: 30px;
    font-weight: 400;
    text-transform: uppercase;
    letter-spacing: 0.5px;
    white-space: nowrap;
    line-height: 1;
  }
  .company-name .accent { color: var(--orange); }
  .rule {
    flex: 1;
    height: 2px;
    background: var(--orange);
    margin-left: 10px;
    margin-top: 2px;
  }
  .services {
    margin-top: 8px;
    font-size: 17px;
    color: var(--orange);
    letter-spacing: 0.3px;
  }
  .contacts {
    position: absolute;
    left: 56px;
    top: 250px;
    list-style: none;
  }
  .contact {
    display: flex;
    align-items: center;
    height: 40px;
    font-size: 22px;
  }
  .contact-name { text-transform: uppercase; font-size: 24px; }
  .contact-icon {
    width: 30px;
    height: 30px;
    margin-right: 18px;
    flex: none;
  }
  .licence-band {
    position: absolute;
    left: 0;
    right: 0;
    bottom: 48px;
    height: 62px;
    background: var(--orange);
    display: flex;
    align-items: center;
    padding-left: 56px;
    color: #fff;
    font-size: 22px;
    font-weight: 700;
  }
</style>
</head>
<body>
<main class="canvas">
  <article class="card">
    <header class="masthead">
      <div class="masthead-row">
        <h1 class="company-name"><span class="accent">The</span> Stone Lantern <span class="accent">Pty Ltd.</span></h1>
        <span class="rule"></span>
      </div>
      <p class="services">Plumbing . Drainage . Gas Fitting . Roofing . Jet Blasting . CCTV .</p>
    </header>

    <ul class="contacts">
      <li class="contact">
        <svg class="contact-icon" viewBox="0 0 30 30" aria-hidden="true">
          <rect x="2" y="2" width="26" height="26" rx="4" fill="var(--orange)"/>
        </svg>
        <span class="contact-name">Gus Palmer</span>
      </li>
      <li class="contact">
        <svg class="contact-icon" viewBox="0 0 30 30" aria-hidden="true">
          <rect x="2" y="7" width="26" height="17" rx="1.5" fill="var(--orange)"/>
          <path d="M3 8 L15 17 L27 8" fill="none" stroke="#fff" stroke-width="2"/>
        </svg>
        <span class="contact-email">thestonelantern@mailbarn.example</span>
      </li>
      <li class="contact">
        <svg class="contact-icon" viewBox="0 0 30 30" aria-hidden="true">
          <path d="M7 4 L11 4 L13 10 L10 12.5 C11.5 16 14 18.5 17.5 20 L20 17 L26 19 L26 23 C26 25 24.5 26 22.5 26 C13 25 5 17 4 7.5 C4 5.5 5 4 7 4 Z" fill="var(--orange)"/>
        </svg>
        <span class="contact-phone">0411827396</span>
      </li>
    </ul>

    <footer class="licence-band">Licence# 861427D</footer>
  </article>
</main>
</body>
</html>
```